Business card design for engineering firm specializing in defense industry.

We need a professional business card design. Something simple but stands out. We are an engineering company specializing in composites in the defense industry.
Industry/Entity Type
Defense
Contact Information for Business Card
A simple black business card with the Varlonix yellow color is what we had in mind but open for other designs.
Colors
ffc214

```html
<!DOCTYPE html>
<html lang="en">
<head>
<meta charset="utf-8">
<title>Varlonix Business Card</title>
<link rel="stylesheet" href="https://fonts.googleapis.com/css2?family=Lato:wght@400;700;900&display=swap">
<style>
  :root {
    --brand-yellow: #ffc214;
    --ink-black: #0b0b0b;
    --paper-white: #ffffff;
    --backdrop: #e9e7e3;
  }
  html, body {
    margin: 0;
    padding: 0;
    width: 1200px;
    height: 1200px;
    overflow: hidden;
    background: var(--backdrop);
    font-family: "Lato", sans-serif;
  }
  .sheet {
    position: relative;
    width: 1200px;
    height: 1200px;
  }
  .card {
    position: absolute;
    left: 150px;
    width: 900px;
    height: 514px;
    box-shadow: 0 10px 28px rgba(0,0,0,0.18);
  }
  .card--front { top: 626px; }
  .card--back { top: 60px; }
  .card svg { display: block; }
  .wordmark { font-family: "Lato", sans-serif; font-weight: 900; }
  .person-name { font-family: "Lato", sans-serif; font-weight: 700; letter-spacing: 1px; }
  .person-title { font-family: "Lato", sans-serif; font-weight: 700; }
  .contact-line { font-family: "Lato", sans-serif; font-weight: 400; }
  .address-line { font-family: "Lato", sans-serif; font-weight: 700; }
</style>
</head>
<body>
<main class="sheet">

  <!-- Back of card: brand side -->
  <section class="card card--back" aria-label="Card back">
    <svg width="900" height="514" viewBox="0 0 900 514">
      <rect class="card-base" width="900" height="514" fill="var(--ink-black)"/>
      <g class="brand-lockup">
        <rect x="268" y="190" width="44" height="44" fill="var(--brand-yellow)"/>
        <text class="wordmark" x="332" y="232" font-size="62" fill="var(--paper-white)">Varlonix</text>
      </g>
      <rect class="address-band" x="0" y="380" width="900" height="62" fill="var(--brand-yellow)"/>
      <text class="address-line" x="450" y="419" font-size="20" fill="var(--ink-black)" text-anchor="middle">18 Ridgeline Avenue Fairbrook, OH 44021</text>
    </svg>
  </section>

  <!-- Front of card: contact side -->
  <section class="card card--front" aria-label="Card front">
    <svg width="900" height="514" viewBox="0 0 900 514">
      <rect class="card-base" width="900" height="514" fill="var(--paper-white)"/>
      <polygon class="accent-stripe-top" points="0,312 900,110 900,136 0,326" fill="var(--brand-yellow)"/>
      <polygon class="dark-panel" points="0,330 900,140 900,514 610,514" fill="var(--ink-black)"/>
      <polygon class="accent-stripe-bottom" points="0,336 600,514 560,514 0,352" fill="var(--brand-yellow)"/>
      <polygon class="accent-corner" points="900,470 900,514 820,514" fill="var(--brand-yellow)"/>

      <g class="brand-lockup">
        <rect x="70" y="92" width="34" height="34" fill="var(--brand-yellow)"/>
        <text class="wordmark" x="120" y="124" font-size="46" fill="var(--ink-black)">Varlonix</text>
      </g>

      <g class="identity">
        <text class="person-name" x="560" y="300" font-size="36" fill="var(--brand-yellow)">DANIEL HARLOW</text>
        <text class="person-title" x="560" y="328" font-size="18" fill="var(--paper-white)">Managing director</text>
        <rect class="name-rule" x="560" y="344" width="150" height="3" fill="var(--brand-yellow)"/>
      </g>

      <g class="contacts" fill="var(--paper-white)">
        <g class="contact-phone">
          <path d="M566 375 q-4 6 2 12 q6 6 12 2 l-3 -4 q-3 2 -6 -1 q-3 -3 -1 -6 z" fill="var(--brand-yellow)"/>
          <text class="contact-line" x="592" y="390" font-size="20">555 210 348</text>
        </g>
        <g class="contact-email">
          <rect x="565" y="409" width="16" height="11" fill="var(--brand-yellow)"/>
          <polyline points="565,409 573,416 581,409" fill="none" stroke="var(--ink-black)" stroke-width="1.5"/>
          <text class="contact-line" x="592" y="422" font-size="20">hello@varlonix.com</text>
        </g>
        <g class="contact-web">
          <circle cx="573" cy="447" r="8" fill="var(--brand-yellow)"/>
          <path d="M565 447 h16 M573 439 v16" stroke="var(--ink-black)" stroke-width="1.2"/>
          <text class="contact-line" x="592" y="454" font-size="20">www.varlonix.com</text>
        </g>
      </g>
    </svg>
  </section>

</main>
</body>
</html>
```